Wedding Thank You post card

We would like to design a thank you post card for our wedding guests.
We want it to be a classic style with our photo and a simple 'Thank you' written and then Tom and Marcia 15.03.2014' Where the writing does not obstruct our image.
We need 140 post cards
Sorry for the delay please find some photos you can use for the design process. One or all photos can be used. Thank you

```html
<!DOCTYPE html>
<html lang="en">
<head>
<meta charset="utf-8">
<title>Wedding Thank You Postcard – Tom &amp; Marcia</title>
<link rel="stylesheet" href="https://fonts.googleapis.com/css2?family=Pacifico&family=Great+Vibes&family=Oswald:wght@300;400&display=swap">
<style>
  :root {
    --aqua: #a9dde0;
    --aqua-deep: #8fcfd3;
    --white: #ffffff;
    --cream: #fbf8dd;
    --sand: #e6dccb;
    --sea: #b9c4c6;
    --sky: #c9c6cc;
  }
  * { margin: 0; padding: 0; box-sizing: border-box; }
  html, body { width: 777px; height: 1200px; overflow: hidden; background: var(--white); }
  .postcard { position: relative; width: 777px; height: 1200px; }

  /* Front: photo side */
  .front { position: absolute; left: 0; top: 0; width: 777px; height: 603px; }
  .front-photo {
    position: absolute; inset: 0;
    background: linear-gradient(180deg, var(--sky) 0%, #dcd6d6 30%, var(--sea) 42%, #ece4d6 55%, var(--sand) 100%);
  }
  .label { position: absolute; left: 189px; top: 214px; width: 404px; height: 152px; }
  .label svg { position: absolute; inset: 0; }
  .label-title {
    position: absolute; left: 0; right: 0; top: 28px; text-align: center;
    font-family: "Pacifico", cursive; font-size: 52px; line-height: 1; color: var(--white);
  }
  .label-names {
    position: absolute; left: 0; right: 0; top: 94px; text-align: center;
    font-family: "Great Vibes", cursive; font-size: 31px; line-height: 1; color: var(--white);
  }
  .label-date {
    position: absolute; left: 122px; top: 137px; width: 162px; height: 20px;
    background: var(--white); color: var(--aqua-deep);
    font-family: "Oswald", sans-serif; font-weight: 300; font-size: 17px; line-height: 20px;
    letter-spacing: 4px; text-align: center;
  }

  /* Back: message side */
  .back { position: absolute; left: 0; top: 603px; width: 777px; height: 597px; background: var(--cream); }
  .greeting { position: absolute; left: 20px; top: 190px; width: 360px; text-align: center; }
  .greeting-title {
    font-family: "Pacifico", cursive; font-size: 56px; line-height: 1; color: var(--aqua);
  }
  .greeting-names {
    font-family: "Great Vibes", cursive; font-size: 34px; line-height: 1; color: var(--aqua);
    margin-top: 8px;
  }
  .greeting-date {
    display: inline-block; margin-top: 6px; width: 174px; height: 20px;
    background: var(--aqua); color: var(--white);
    font-family: "Oswald", sans-serif; font-weight: 300; font-size: 17px; line-height: 20px; letter-spacing: 4px;
  }
  .divider {
    position: absolute; left: 400px; top: 90px; width: 22px; height: 368px;
    background: linear-gradient(90deg, transparent 30%, var(--aqua) 30%, var(--aqua) 70%, transparent 70%);
    opacity: .8;
  }
  .stamp-heart { position: absolute; left: 637px; top: 70px; width: 76px; height: 70px; }
  .address-line { position: absolute; left: 489px; width: 238px; height: 2px; background: var(--aqua); }
  .address-line.one { top: 260px; }
  .address-line.two { top: 300px; }
  .address-line.three { top: 333px; }
</style>
</head>
<body>
<main class="postcard">
  <section class="front">
    <div class="front-photo" role="img" aria-label="Photograph of the bride and groom walking hand in hand along the beach toward the sea"></div>
    <div class="label">
      <svg viewBox="0 0 404 152" width="404" height="152" aria-hidden="true">
        <path d="M40 8 H364 Q372 28 392 30 Q404 76 392 122 Q372 124 364 144 H40 Q32 124 12 122 Q0 76 12 30 Q32 28 40 8 Z" fill="var(--aqua)"/>
      </svg>
      <div class="label-title">Thank you</div>
      <div class="label-names">Tom &amp; Marcia</div>
      <div class="label-date">15.03.2014</div>
    </div>
  </section>

  <section class="back">
    <div class="greeting">
      <div class="greeting-title">Thank you</div>
      <div class="greeting-names">Tom &amp; Marcia</div>
      <div class="greeting-date">15.03.2014</div>
    </div>
    <div class="divider" role="img" aria-label="Vertical ornamental flourish dividing message and address"></div>
    <svg class="stamp-heart" viewBox="0 0 76 70" aria-hidden="true">
      <path d="M38 68 C14 50 2 36 2 20 C2 9 11 2 21 2 C29 2 35 7 38 13 C41 7 47 2 55 2 C65 2 74 9 74 20 C74 36 62 50 38 68 Z" fill="var(--aqua)"/>
    </svg>
    <div class="address-line one"></div>
    <div class="address-line two"></div>
    <div class="address-line three"></div>
  </section>
</main>
</body>
</html>
```